Vision Board Class Design needed

Hello, I need a business card design for a new Company based in Mount Waverley, Victoria, Australia. The Company provides a training Class with approx. 5 guests. They learn how to choose and create positive things in their life. It is based on the principal of the Law of Attraction. Each guest receives a large coloured cardboard and magazines, affirmations to choose ideas to help create their new exciting life - all pasted onto a "Vision Board" which will be seen by them every day and help to clarify the vision and attract abundance, happiness & positivity into their lives. I would like to see designs with bright, happy colours - perhaps rainbows - anything that represents a new life and appears refreshing.
Many thanks.

Industry/Entity Type

Training

Contact Information for Business Card

Dream Harbour
Lorna
Mobile 0473 259-386

Logo Text

Dream Harbour

Logo styles of interest
Abstract Logo
Requirements
Must have
• Happy, Bright colours!

```html
<!DOCTYPE html>
<html lang="en">
<head>
<meta charset="utf-8">
<title>Dream Harbour — Business Card</title>
<link rel="stylesheet" href="https://fonts.googleapis.com/css2?family=Arimo:wght@700&display=swap">
<style>
  :root {
    --backdrop: #2a2a2a;
    --red: #d51f26;
    --orange: #f0652b;
    --yellow: #f7e62a;
    --green: #1fb34b;
    --pale: #e9f3e6;
    --sky: #4a8fcd;
    --navy: #2b2a78;
    --indigo: #26307c;
    --purple: #3a2d8c;
    --white: #ffffff;
  }
  html, body {
    margin: 0;
    width: 1200px;
    height: 900px;
    overflow: hidden;
    background: var(--backdrop);
  }
  .canvas {
    width: 1200px;
    height: 900px;
    display: flex;
    flex-direction: column;
    align-items: center;
    justify-content: center;
    gap: 40px;
  }
  .business-card {
    width: 640px;
    height: 391px;
    display: block;
    box-shadow: 0 10px 30px rgba(0, 0, 0, 0.5);
  }
  .card-type {
    font-family: "Arimo", Arial, sans-serif;
    font-weight: 700;
  }
  .tone-red { stop-color: var(--red); }
  .tone-orange { stop-color: var(--orange); }
  .tone-yellow { stop-color: var(--yellow); }
  .tone-green { stop-color: var(--green); }
  .tone-pale { stop-color: var(--pale); }
  .tone-sky { stop-color: var(--sky); }
  .tone-navy { stop-color: var(--navy); }
  .tone-indigo { stop-color: var(--indigo); }
  .tone-purple { stop-color: var(--purple); }
  .brand-name { fill: var(--white); font-size: 38px; letter-spacing: 0.5px; }
  .person-name { fill: var(--red); font-size: 54px; }
  .phone-number { fill: var(--green); font-size: 46px; }
  .phone-label { fill: var(--green); font-size: 17px; }
</style>
</head>
<body>
<main class="canvas">

  <svg class="business-card card-front" viewBox="0 0 640 391" aria-label="Dream Harbour business card front">
    <defs>
      <clipPath id="front-clip"><rect width="640" height="391"/></clipPath>
      <linearGradient id="front-wash" gradientUnits="userSpaceOnUse" x1="-380" y1="0" x2="395" y2="0">
        <stop offset="0.08" class="tone-red"/>
        <stop offset="0.23" class="tone-orange"/>
        <stop offset="0.35" class="tone-yellow"/>
        <stop offset="0.47" class="tone-green"/>
        <stop offset="0.58" class="tone-sky"/>
        <stop offset="0.70" class="tone-navy"/>
        <stop offset="0.88" class="tone-purple"/>
      </linearGradient>
    </defs>
    <g clip-path="url(#front-clip)">
      <g transform="translate(320 195) rotate(30)">
        <rect class="rainbow-artwork" role="img" aria-label="Decorative diagonal rainbow artwork"
              x="-380" y="-520" width="775" height="1040" fill="url(#front-wash)"/>
        <text class="card-type brand-name" transform="translate(-17.5 0) rotate(-90)"
              text-anchor="middle" dominant-baseline="central">DREAM HARBOUR</text>
      </g>
    </g>
  </svg>

  <svg class="business-card card-back" viewBox="0 0 640 391" aria-label="Dream Harbour business card back">
    <defs>
      <clipPath id="back-clip"><rect width="640" height="391"/></clipPath>
      <linearGradient id="back-wash" gradientUnits="userSpaceOnUse" x1="0" y1="-340" x2="0" y2="335">
        <stop offset="0.10" class="tone-red"/>
        <stop offset="0.26" class="tone-orange"/>
        <stop offset="0.37" class="tone-yellow"/>
        <stop offset="0.49" class="tone-pale"/>
        <stop offset="0.61" class="tone-sky"/>
        <stop offset="0.72" class="tone-indigo"/>
        <stop offset="0.89" class="tone-purple"/>
      </linearGradient>
    </defs>
    <g clip-path="url(#back-clip)">
      <g transform="translate(320 195) rotate(22)">
        <rect class="rainbow-artwork" role="img" aria-label="Decorative diagonal rainbow artwork"
              x="-520" y="-340" width="1040" height="675" fill="url(#back-wash)"/>
        <text class="card-type person-name" x="160" y="-62" text-anchor="end">LORNA</text>
        <text class="card-type phone-label" x="168" y="-32" text-anchor="end">MOBILE</text>
        <text class="card-type phone-number" x="178" y="18" text-anchor="end">0473 259-386</text>
      </g>
    </g>
  </svg>

</main>
</body>
</html>
```